Quenderil - Still Grace Cosmetics

Please design a logo and business cards for new food supplements, cosmetics and herbal fixatives. The products are produced ecologically and biologically in the South Tyrol and Trentino alps. The products are pure and noble. Quenderil = pure vitality Colors Background: dark or black matt (soft touch) Logodesign: powerful, elegant, violet with glossy foil The logo and design should convey warmth, passion and the 6th sense, you should get the impression that you can smell the herbal odor , Logo and business cards for new food supplements, cosmetics and herbal fixatives. The products are produced ecologically and biologically in the South Tyrol and Trentino alps. The products are pure and noble. Quenderil = pure vitality Colors Background: dark or black matt (softtouch) Logodesign: powerful elegant violet with glossy foil The logo and design is meant to convey warmth, passion and the 6th sense, you should get the impression that you can smell the herbal perfume.

Target Market(s)

Food, food supplements, vitality, health

Contact Information for Business Card

Please provide an elegant darf design that is puristic, but has a very good logo design
Elegantes dunkles design, puristisch

Logo Text

Quenderil - still Grace

Colors
6b449b

Requirements
Must have
• SVG Files Alpha channel for foil embossing High-quality design
Nice to have
• Pure elegance
Should not have
• to colorful colors

```html
<!DOCTYPE html>
<html lang="en">
<head>
<meta charset="utf-8">
<title>Quenderil – Business Card</title>
<link href="https://fonts.googleapis.com/css2?family=Didact+Gothic&family=Arimo&display=swap" rel="stylesheet">
<style>
  :root {
    --backdrop: #8f8f8f;
    --card: #262626;
    --card-emboss: #2d2d2d;
    --emboss-line: #1c1c1c;
    --ink-grey: #858585;
    --ink-soft: #6f6f6f;
    --divider: #4a4a4a;
    --violet: #8a4fc7;
    --caption: #6a6a6a;
  }
  * { margin: 0; padding: 0; box-sizing: border-box; }
  html, body {
    width: 1200px;
    height: 1038px;
    overflow: hidden;
    background: var(--backdrop);
  }
  .stage {
    position: relative;
    width: 1200px;
    height: 1038px;
  }
  .finish-caption {
    position: absolute;
    top: 62px;
    left: 0;
    width: 1200px;
    text-align: center;
    font-family: "Arimo", Arial, sans-serif;
    font-size: 14px;
    color: var(--caption);
  }
  .card {
    position: absolute;
    left: 309px;
    width: 601px;
    height: 332px;
    background: var(--card);
    border-radius: 14px;
  }
  .card--front { top: 140px; }
  .card--back { top: 590px; }

  .brand {
    position: absolute;
    left: 86px;
    top: 90px;
    width: 200px;
    text-align: center;
  }
  .brand-dot {
    display: block;
    width: 84px;
    height: 84px;
    margin: 0 auto 38px;
    border-radius: 50%;
    background: var(--violet);
  }
  .brand-name {
    font-family: "Didact Gothic", sans-serif;
    font-size: 19px;
    letter-spacing: 5px;
    color: var(--violet);
  }
  .divider {
    position: absolute;
    left: 294px;
    top: 90px;
    width: 1px;
    height: 143px;
    background: var(--divider);
  }
  .contact {
    position: absolute;
    left: 329px;
    top: 88px;
    font-family: "Didact Gothic", sans-serif;
    color: var(--ink-grey);
    text-transform: uppercase;
  }
  .contact-name {
    font-size: 18px;
    letter-spacing: 0.5px;
    line-height: 22px;
  }
  .contact-role {
    font-size: 11px;
    letter-spacing: 0.6px;
    color: var(--ink-soft);
    line-height: 14px;
    margin-bottom: 16px;
  }
  .contact-lines {
    font-size: 11px;
    letter-spacing: 0.8px;
    line-height: 16px;
    color: var(--ink-soft);
    margin-bottom: 14px;
  }

  .emboss {
    position: absolute;
    left: 0;
    top: 0;
    width: 601px;
    height: 332px;
  }
</style>
</head>
<body>
<main class="stage">
  <p class="finish-caption">Embossing&nbsp; + foil stamping</p>

  <section class="card card--front" aria-label="Business card front">
    <div class="brand">
      <span class="brand-dot"></span>
      <div class="brand-name">QUENDERIL</div>
    </div>
    <div class="divider"></div>
    <div class="contact">
      <div class="contact-name">Mira Solvenholt</div>
      <div class="contact-role">General Manager</div>
      <div class="contact-lines">
        +43 650 48273915<br>
        info@quenderil.com<br>
        www.quenderil.com
      </div>
      <div class="contact-lines">
        Lerchenpfad 12<br>
        4720 Almtalried
      </div>
    </div>
  </section>

  <section class="card card--back" aria-label="Business card back with blind embossing">
    <svg class="emboss" viewBox="0 0 601 332" aria-hidden="true">
      <circle cx="300" cy="166" r="130" fill="none" stroke="var(--emboss-line)" stroke-width="2"/>
      <text x="300" y="175" text-anchor="middle" font-family="Didact Gothic, sans-serif" font-size="34" letter-spacing="8" fill="var(--card-emboss)">QUENDERIL</text>
    </svg>
  </section>
</main>
</body>
</html>
```